Current state of Man's Soul Christian view

I would like an improvement of my design or a reimagining of my design to help people visualize what happens to the soul after we die. The second picture "screenshot 2023" is not my design but gives another idea.

For further information, there are 4 "time" frames that could be sectioned off. Eden is one time. Then adam rebellion and pre messiah earth (with hades/ Sheol). The third time frame is Jesus death, resurrection with the current state of earth. The 4th time frame is the "heavenly realm" which is across all 3 times and is unchanged.

For color ideas, please see my website www.brightlanternpath.org which has my color theme. But the death of Jesus I would like in some type of red as well as the death of believers.

My goal is something simple, engaging, and easy to understand. If you have any questions please lmk.
Thank you for considering my project.

```html
<!DOCTYPE html>
<html lang="en">
<head>
<meta charset="utf-8">
<title>Current State of Man's Soul</title>
<link rel="stylesheet" href="https://fonts.googleapis.com/css2?family=Oswald:wght@400;500;600&family=Roboto+Condensed:wght@500&display=swap">
<style>
  :root {
    --navy: #14203a;
    --navy-edge: #2a3a5c;
    --gold: #e6bf4f;
    --gold-light: #f4d86a;
    --gold-edge: #b88f2a;
    --red: #b3161c;
    --red-edge: #d23b3b;
    --teal: #0fb3b1;
    --white: #ffffff;
    --arrow-edge: #8a8f99;
    --era-tint-a: rgba(255,255,255,0.07);
    --era-tint-b: rgba(10,20,40,0.07);
    --era-line: rgba(255,255,255,0.55);
  }
  * { box-sizing: border-box; }
  html, body {
    margin: 0;
    padding: 0;
    width: 1200px;
    height: 925px;
    overflow: hidden;
  }
  .canvas {
    position: relative;
    width: 1200px;
    height: 925px;
    overflow: hidden;
    font-family: "Oswald", sans-serif;
    color: var(--white);
  }
  .sky {
    position: absolute;
    inset: 0;
    background: linear-gradient(180deg,
      #e3a23a 0%, #f2cd6c 11%, #fbeed6 23%, #eef0f2 30%,
      #5a5f72 35%, #262f48 41%, #2b3a58 50%,
      #7ea7cf 57%, #a8c7e3 66%, #f0d9bd 74%,
      #ec9543 83%, #c2481c 92%, #7d2410 100%);
  }
  .palace {
    position: absolute;
    left: 290px; top: 48px;
    width: 590px; height: 225px;
    border-radius: 120px 120px 30px 30px;
    background: radial-gradient(ellipse at 50% 40%, #f7d77a 0%, #dba33a 55%, rgba(235,190,90,0) 80%);
  }

  /* time-frame sections */
  .era {
    position: absolute;
    top: 285px; bottom: 0;
  }
  .era--eden { left: 0; width: 180px; background: var(--era-tint-a); }
  .era--fall { left: 180px; width: 330px; background: var(--era-tint-b); border-left: 2px dashed var(--era-line); }
  .era--cross { left: 510px; right: 0; background: var(--era-tint-a); border-left: 2px dashed var(--era-line); }
  .era--heaven {
    top: 0; left: 0; right: 0; height: 285px; bottom: auto;
    border-bottom: 2px dashed var(--era-line);
  }
  .era-label {
    position: absolute;
    transform: translateX(-50%);
    padding: 2px 12px;
    border-radius: 12px;
    background: rgba(20,32,58,0.82);
    font-size: 14px;
    font-weight: 500;
    letter-spacing: 1px;
    text-transform: uppercase;
    white-space: nowrap;
  }

  .title {
    position: absolute;
    top: 8px; left: 0; width: 1200px;
    margin: 0;
    text-align: center;
    font-weight: 600;
    font-size: 45px;
    line-height: 1.2;
    text-shadow: 0 2px 6px rgba(120,70,0,0.55);
  }
  .brand {
    position: absolute;
    left: 0; top: 119px;
    width: 294px; height: 102px;
    background: var(--teal);
    padding: 16px 0 0 22px;
  }
  .brand-name {
    display: flex; align-items: center; gap: 10px;
    font-size: 27px; font-weight: 400; line-height: 1;
  }
  .brand-dot {
    width: 22px; height: 22px; border-radius: 50%;
    background: var(--white);
  }
  .brand-url {
    margin-top: 18px;
    padding-left: 42px;
    font-family: "Roboto Condensed", sans-serif;
    font-weight: 500; font-size: 20px;
  }
  .links, .arrows {
    position: absolute; inset: 0;
  }
  .photo {
    position: absolute;
    border-radius: 50%;
    border: 4px solid var(--white);
    box-shadow: 0 3px 10px rgba(0,0,0,0.35);
    transform: translate(-50%, -50%);
  }
  .photo--red { border-color: var(--red-edge); }
  .tag {
    position: absolute;
    transform: translate(-50%, -50%);
    display: flex; align-items: center; justify-content: center;
    text-align: center;
    background: var(--navy);
    border: 2px solid var(--navy-edge);
    border-radius: 22px;
    font-weight: 500;
    font-size: 24px;
    line-height: 1.1;
    white-space: nowrap;
  }
  .tag--small { font-size: 22px; }
  .tag--gold { background: var(--gold); border-color: var(--gold-light); color: #fff8dc; text-shadow: 0 1px 2px rgba(90,60,0,0.6); }
  .tag--red { background: var(--red); border-color: var(--red-edge); }
  .realm {
    position: absolute;
    transform: translateX(-50%);
    text-align: center;
    line-height: 1;
    white-space: nowrap;
  }
  .realm-name {
    display: block;
    font-size: 46px; font-weight: 400;
    color: rgba(255,255,255,0.85);
    text-shadow: 0 0 2px rgba(120,120,120,0.7);
  }
  .realm-sub {
    display: block; margin-top: 2px;
    font-size: 25px;
    color: rgba(255,255,255,0.88);
    text-shadow: 0 1px 2px rgba(80,80,80,0.6);
  }
  .realm--torment .realm-name { color: #fff; font-weight: 500; text-shadow: 0 2px 4px rgba(120,30,0,0.6); }
  .heaven-label {
    position: absolute;
    left: 598px; top: 304px;
    transform: translate(-50%, -50%);
    font-size: 27px;
    white-space: nowrap;
  }
</style>
</head>
<body>
<div class="canvas">
  <div class="sky" role="img" aria-label="Sky rising from fiery red clouds below, through blue sky and starry space, to golden clouds above"></div>
  <div class="palace" role="img" aria-label="Golden heavenly palace among clouds"></div>

  <div class="era era--heaven"></div>
  <div class="era era--eden"></div>
  <div class="era era--fall"></div>
  <div class="era era--cross"></div>

  <h1 class="title">3rd Heaven - God's Heavenly Throne</h1>

  <div class="brand">
    <div class="brand-name"><span class="brand-dot"></span>Bright Lantern Path</div>
    <div class="brand-url">brightlanternpath.org</div>
  </div>

  <div class="era-label" style="left:147px;top:236px;">4 · Heavenly Realm · all times</div>
  <div class="era-label" style="left:90px;top:896px;">1 · Eden</div>
  <div class="era-label" style="left:455px;top:896px;">2 · Fall &amp; Sheol</div>
  <div class="era-label" style="left:1090px;top:896px;">3 · Cross &amp; Today</div>

  <svg class="links" width="1200" height="925" viewBox="0 0 1200 925">
    <g fill="none" stroke="#ffffff" stroke-width="3">
      <polyline points="260,548 260,813 300,813"/>
      <line x1="260" y1="619" x2="300" y2="619"/>
      <line x1="957" y1="390" x2="1000" y2="390"/>
      <polyline points="901,443 901,623 1000,623"/>
    </g>
  </svg>

  <div class="photo" style="left:95px;top:388px;width:144px;height:144px;background:linear-gradient(160deg,#9fc3c9,#3f7d5a 55%,#2b5a3a)" role="img" aria-label="Lush garden of Eden with lake and mountains"></div>
  <div class="photo" style="left:260px;top:388px;width:126px;height:126px;background:radial-gradient(circle at 50% 40%,#c98a4a,#6b3a1c 70%)" role="img" aria-label="Adam and Eve leaving the garden"></div>
  <div class="photo" style="left:262px;top:492px;width:112px;height:112px;background:radial-gradient(circle,#fff6d8 0%,#b8a77a 25%,#2c2c2a 70%)" role="img" aria-label="Tunnel of light at death"></div>
  <div class="photo" style="left:420px;top:388px;width:126px;height:126px;background:linear-gradient(180deg,#b9cfe0,#c9a779 45%,#6e4d30)" role="img" aria-label="Crowded ancient marketplace"></div>
  <div class="photo" style="left:600px;top:384px;width:126px;height:126px;background:radial-gradient(circle at 50% 40%,#ffffff,#e8dcc4 35%,#8eb3d2 75%)" role="img" aria-label="Risen Jesus in white robes"></div>
  <div class="photo" style="left:600px;top:614px;width:180px;height:180px;border-width:0;background:radial-gradient(circle at 50% 40%,#f7a040,#c43c14 55%,#4a1208)" role="img" aria-label="Cross on a hill against a burning sky"></div>
  <div class="photo" style="left:786px;top:185px;width:112px;height:112px;background:radial-gradient(circle at 50% 45%,#ffffff,#9cc4ec 55%,#3d7cc4)" role="img" aria-label="White dove descending"></div>
  <div class="photo" style="left:787px;top:384px;width:122px;height:122px;background:linear-gradient(180deg,#c9d0d6,#7d8790 50%,#3f4548)" role="img" aria-label="Polluted industrial city"></div>
  <div class="photo photo--red" style="left:903px;top:390px;width:112px;height:112px;background:radial-gradient(circle,#fff2dc 0%,#c98a6a 25%,#4a1410 70%)" role="img" aria-label="Tunnel of light at a believer's death"></div>
  <div class="photo" style="left:1088px;top:388px;width:184px;height:184px;background:radial-gradient(circle at 50% 35%,#fffbe6,#f0c468 35%,#8a5a24 80%)" role="img" aria-label="Believers embracing in radiant light"></div>
  <div class="photo" style="left:1088px;top:623px;width:180px;height:180px;background:radial-gradient(circle,#b46a4a,#5a2a1c 70%)" role="img" aria-label="Anguished crowd"></div>
  <div class="photo" style="left:336px;top:619px;width:90px;height:90px;background:radial-gradient(circle,#e8eef4,#6a7d92 55%,#2a3340)" role="img" aria-label="Narrow gate opening to light"></div>
  <div class="photo" style="left:336px;top:808px;width:90px;height:90px;background:radial-gradient(circle,#f0823a,#7a2a14 60%,#2a0e08)" role="img" aria-label="Wide gate glowing with fire"></div>

  <svg class="arrows" width="1200" height="925" viewBox="0 0 1200 925">
    <g fill="#ffffff" stroke="var(--arrow-edge)" stroke-width="1.5">
      <polygon points="158,382 187,382 187,373 205,390 187,407 187,398 158,398"/>
      <polygon points="320,382 348,382 348,373 366,390 348,407 348,398 320,398"/>
      <polygon points="372,612 390,612 390,603 406,619 390,635 390,626 372,626"/>
      <polygon points="372,801 390,801 390,792 406,808 390,824 390,815 372,815"/>
      <polygon transform="translate(479,501) rotate(38)" points="0,-8 62,-8 62,-17 80,0 62,17 62,8 0,8"/>
      <polygon transform="translate(600,528) rotate(-90)" points="0,-7 17,-7 17,-15 31,0 17,15 17,7 0,7"/>
      <polygon transform="translate(787,294) rotate(90)" points="0,-7 20,-7 20,-16 36,0 20,16 20,7 0,7"/>
      <polygon transform="translate(989,668) rotate(135)" points="0,-14 109,-14 109,-28 147,0 109,28 109,14 0,14"/>
    </g>
    <g fill="var(--gold-light)" stroke="var(--gold-edge)" stroke-width="1.5">
      <polygon transform="translate(603,271) rotate(-90)" points="0,-18 111,-18 111,-30 145,0 111,30 111,18 0,18"/>
      <polygon transform="translate(1082,271) rotate(-90)" points="0,-18 111,-18 111,-30 145,0 111,30 111,18 0,18"/>
      <polygon transform="translate(787,75) rotate(90)" points="0,-16 35,-16 35,-28 63,0 35,28 35,16 0,16"/>
    </g>
  </svg>

  <div class="tag" style="left:94px;top:460px;width:100px;height:42px;">Eden</div>
  <div class="tag" style="left:262px;top:324px;width:190px;height:45px;">Adam Rebellion</div>
  <div class="tag" style="left:260px;top:548px;width:90px;height:40px;">Death</div>
  <div class="tag" style="left:420px;top:470px;width:167px;height:68px;border-radius:30px;">Pre-messiah<br>Fallen Earth</div>
  <div class="tag tag--gold" style="left:600px;top:460px;width:170px;height:72px;border-radius:34px;">Jesus<br>Resurrection</div>
  <div class="tag tag--red" style="left:600px;top:700px;width:170px;height:43px;">Jesus death</div>
  <div class="tag tag--gold tag--small" style="left:786px;top:260px;width:135px;height:62px;border-radius:28px;">Holy Spirit<br>Descents</div>
  <div class="tag" style="left:787px;top:470px;width:158px;height:68px;border-radius:30px;">Current<br>Fallen Earth</div>
  <div class="tag tag--red" style="left:903px;top:333px;width:92px;height:40px;">Death</div>
  <div class="tag" style="left:1088px;top:459px;width:158px;height:72px;border-radius:34px;">In Jesus<br>Believers</div>
  <div class="tag" style="left:1088px;top:698px;width:176px;height:43px;">Non-Believers</div>
  <div class="tag tag--small" style="left:337px;top:673px;width:140px;height:40px;">Narrow gate</div>
  <div class="tag tag--small" style="left:337px;top:862px;width:140px;height:40px;">Wide gate</div>

  <div class="heaven-label">2nd Heaven</div>

  <div class="realm" style="left:495px;top:578px;"><span class="realm-name">Paradise</span><span class="realm-sub">1st Heaven</span></div>
  <div class="realm" style="left:802px;top:578px;"><span class="realm-name">Paradise</span><span class="realm-sub">1st Heaven</span></div>
  <div class="realm realm--torment" style="left:492px;top:774px;"><span class="realm-name">Torment</span><span class="realm-sub">Hades/Sheol</span></div>
  <div class="realm realm--torment" style="left:799px;top:774px;"><span class="realm-name">Torment</span><span class="realm-sub">Hades/Sheol</span></div>
</div>
</body>
</html>
```